Business Cards & Stationery
Hollowmere Capital Group (Investment Firm)
Project: Business Cards & Stationery
Business Cards & Stationery  -
Creative Brief
Professional
Peter L. Vanstrom III
Registered Principal, OSJ
917 Larkspur Road Milbrook, WV 25418
peter.vanstrom@quillmark-example.com
www.HollowmereCapitalGroup-example.com
Also has to say (in smaller font): Securities and advisory services offered through Crestfield Ledger Corporation (CLC). Member TVORA/BQLX and a Registered Investment Advisor. Hollowmere Capital Group and CLC are separate and unrelated companies.
logo for Hollowmere Capital Group

```html
<!DOCTYPE html>
<html lang="en">
<head>
<meta charset="utf-8">
<title>Hollowmere Capital Group — Business Cards</title>
<link rel="stylesheet" href="https://fonts.googleapis.com/css2?family=Cinzel:wght@500&family=Tinos:wght@400;700&display=swap">
<style>
  :root {
    --navy: #2f4a7d;
    --grey-card: #a9aaad;
    --paper: #ffffff;
    --ink: #3a3a3a;
    --ink-soft: #666a70;
    --rule: #c7c9cc;
    --gap: #ffffff;
  }
  * { box-sizing: border-box; margin: 0; padding: 0; }
  html, body { width: 1200px; height: 689px; overflow: hidden; background: var(--gap); }
  .sheet { position: relative; width: 1200px; height: 689px; }
  .card { position: absolute; overflow: hidden; }
  .card-front { left: 0; top: 0; width: 629px; height: 336px; background: var(--paper); }
  .card-navy-top { left: 643px; top: 0; width: 557px; height: 336px; background: var(--navy); }
  .card-navy-bottom { left: 0; top: 353px; width: 629px; height: 336px; background: var(--navy); }
  .card-grey { left: 643px; top: 353px; width: 557px; height: 336px; background: var(--grey-card); }

  .edge-strip { position: absolute; right: 0; top: 0; width: 22px; height: 100%; background: var(--navy); }
  .edge-rule { position: absolute; right: 26px; top: 0; width: 3px; height: 100%; background: var(--rule); }

  .brand { display: flex; align-items: center; gap: 16px; font-family: "Cinzel", serif; font-weight: 500; }
  .brand-square { width: 30px; height: 30px; background: currentColor; flex: none; }
  .brand-name { line-height: 1.15; letter-spacing: 0.06em; font-size: 27px; }
  .brand-name span { display: block; }

  .card-front .brand { position: absolute; left: 52px; top: 22px; color: var(--navy); }
  .card-front .brand-name { font-size: 24px; }
  .card-front .brand-square { width: 26px; height: 26px; }

  .centered { position: absolute; inset: 0; display: flex; align-items: center; justify-content: center; color: #ffffff; }

  .holder { position: absolute; left: 64px; top: 226px; font-family: "Tinos", serif; }
  .holder-name { color: var(--navy); font-weight: 700; font-size: 17px; }
  .holder-title { color: var(--ink-soft); font-size: 13px; margin-top: 6px; }

  .contact { position: absolute; left: 318px; top: 172px; font-family: "Tinos", serif; font-style: normal; font-size: 11.5px; color: var(--ink); line-height: 1.45; }
  .contact .label { font-weight: 700; }

  .disclaimer { position: absolute; left: 52px; top: 290px; width: 530px; font-family: "Tinos", serif; font-size: 8.5px; line-height: 1.35; color: var(--ink-soft); }
</style>
</head>
<body>
<main class="sheet">
  <section class="card card-front" aria-label="Business card front">
    <div class="brand">
      <div class="brand-square"></div>
      <div class="brand-name"><span>Hollowmere</span><span>Capital Group</span></div>
    </div>
    <div class="holder">
      <p class="holder-name">Peter L. Vanstrom III</p>
      <p class="holder-title">Registered Principal, OSJ</p>
    </div>
    <address class="contact">
      <p>917 Larkspur Road</p>
      <p>Milbrook, WV 25418</p>
      <p><span class="label">Phone :</span> 304 555 0142</p>
      <p><span class="label">Fax :</span> 304 555 0187</p>
      <p><span class="label">Email :</span> peter.vanstrom@quillmark-example.com</p>
      <p><span class="label">Web :</span> www.HollowmereCapitalGroup-example.com</p>
    </address>
    <p class="disclaimer">Securities and advisory services offered through Crestfield Ledger Corporation (CLC). Member TVORA/BQLX and a Registered Investment Advisor. Hollowmere Capital Group and CLC are separate and unrelated companies.</p>
    <div class="edge-rule"></div>
    <div class="edge-strip"></div>
  </section>

  <section class="card card-navy-top" aria-label="Business card back, navy">
    <div class="centered">
      <div class="brand">
        <div class="brand-square"></div>
        <div class="brand-name"><span>Hollowmere</span><span>Capital Group</span></div>
      </div>
    </div>
  </section>

  <section class="card card-navy-bottom" aria-label="Business card back, navy alternate">
    <div class="centered">
      <div class="brand">
        <div class="brand-square"></div>
        <div class="brand-name"><span>Hollowmere</span><span>Capital Group</span></div>
      </div>
    </div>
  </section>

  <section class="card card-grey" aria-label="Business card back, grey">
    <div class="centered">
      <div class="brand">
        <div class="brand-square"></div>
        <div class="brand-name"><span>Hollowmere</span><span>Capital Group</span></div>
      </div>
    </div>
  </section>
</main>
</body>
</html>
```